School Rules Posters

I would like a design for four different posters. Each one has a different purpose:

1: The Three Main rules

2: The Rewards

3: The Consequences

4: Consequences

At the moment they are very boring and dry and I would like an icon for each rule with the text underneath?

I'd like the logo on it.

It is for a middle school so it cannot be 'too young'.

I don't mind if the posters are Portrait or Landscape. The posters need to provide pupils with clarity and cannot be too busy. They'll be made into A1.
I have attached an example from another school which has logos - I don't want the same thing but give's you an idea of icons.

```html
<!DOCTYPE html>
<html lang="en">
<head>
<meta charset="utf-8">
<title>The Aldwick Way – Posters</title>
<link href="https://fonts.googleapis.com/css2?family=Oswald:wght@500;600&family=Lato:wght@400;700;900&display=swap" rel="stylesheet">
<style>
:root{
  --backdrop:#6b666e;
  --plum:#3e2230;
  --magenta:#9b2a8a;
  --bright:#b52fa0;
  --orchid:#a34d96;
  --grape:#6e2a5f;
  --deep:#5e2350;
  --mauve:#8a6f86;
  --lavender:#e7dde6;
  --paper:#ffffff;
  --ink:#3a2a35;
}
*{box-sizing:border-box;margin:0;padding:0}
html,body{width:786px;height:1200px;overflow:hidden}
body{background:var(--backdrop);position:relative;font-family:"Lato",Arial,sans-serif;color:var(--ink)}
.poster{position:absolute;background:var(--paper);overflow:hidden}
.poster-rules{left:29px;top:84px;width:350px;height:491px}
.poster-rewards{left:402px;top:84px;width:348px;height:491px}
.poster-consequences{left:29px;top:625px;width:720px;height:510px}

.kicker{position:absolute;left:0;right:0;top:0;height:21px;text-align:center;font-weight:700;font-size:11.5px;line-height:21px;letter-spacing:.3px;color:var(--plum)}
.title-band{position:absolute;left:0;right:0;top:21px;height:43px;background:var(--plum);text-align:center}
.title{font-family:"Oswald",Impact,sans-serif;font-weight:600;color:#fff;font-size:34px;line-height:43px;letter-spacing:.5px}
.motto{position:absolute;left:0;right:0;top:64px;height:20px;background:var(--magenta);color:#fff;text-align:center;font-weight:700;font-size:9.5px;line-height:20px}
.brand{position:absolute;left:10px;top:28px;display:flex;align-items:center;gap:5px;z-index:2}
.brand-square{width:10px;height:10px;background:#fff}
.brand-name{color:#fff;font-weight:700;font-size:7px;line-height:1.15;width:44px}

.footer{position:absolute;left:0;right:0;bottom:6px;height:21px;background:var(--plum);color:#fff;text-align:center;font-weight:700;font-size:8px;line-height:23px}
.footer-strip{position:absolute;left:0;right:0;bottom:0;height:6px;background:var(--magenta)}
.globe{position:absolute;left:50%;top:-6px;width:12px;height:12px;margin-left:-6px;border-radius:50%;background:var(--magenta);border:1.5px solid #fff}

/* Rules */
.rule{position:absolute;top:98px;width:101px}
.rule-ready{left:14px}.rule-respect{left:127px}.rule-safe{left:238px}
.rule-column{position:absolute;left:5px;top:45px;width:91px;height:305px;background:var(--lavender);border-radius:0 0 46px 46px}
.rule-pennant{position:absolute;left:25px;top:0;width:51px;height:64px;clip-path:polygon(0 0,100% 0,100% 72%,50% 100%,0 72%);display:flex;justify-content:center;padding-top:12px}
.rule-label{position:absolute;left:0;top:71px;width:101px;height:34px;border:2px solid var(--paper);outline:2px solid currentColor;color:#fff;text-align:center;font-weight:700;font-size:11px;line-height:1.05;display:flex;align-items:center;justify-content:center}
.rule-list{position:absolute;left:13px;top:112px;width:75px;list-style:none;text-align:center;font-size:7.6px;line-height:1.3}
.rule-list li{padding:5px 0 6px;border-bottom:1px dotted var(--mauve)}
.rule-list li:last-child{border-bottom:none}
.rule-ready .rule-list li{padding:7px 0 9px}
.tone-mauve{background:var(--mauve);color:var(--mauve)}
.tone-magenta{background:var(--magenta);color:var(--magenta)}
.tone-deep{background:var(--deep);color:var(--deep)}

/* Rewards */
.reward{position:absolute;width:133px;height:148px;color:#fff;text-align:center;border-radius:0 0 66px 66px/0 0 26px 26px;padding:33px 9px 0}
.reward-house{left:20px;top:122px;background:var(--mauve)}
.reward-council{left:193px;top:122px;background:var(--magenta)}
.reward-subject{left:20px;top:306px;background:var(--grape)}
.reward-head{left:193px;top:306px;background:var(--plum)}
.reward-badge{position:absolute;left:50%;top:-24px;width:46px;height:46px;margin-left:-23px;border-radius:50%;background:#fff;border:2px solid currentColor;display:flex;align-items:center;justify-content:center}
.reward-house .reward-badge{color:var(--mauve)}.reward-council .reward-badge{color:var(--magenta)}
.reward-subject .reward-badge{color:var(--grape)}.reward-head .reward-badge{color:var(--plum)}
.reward h3{font-size:9.5px;font-weight:700;line-height:1.05;margin-top:4px}
.reward .points{font-size:7px;font-weight:900;margin:4px 0 3px}
.reward p{font-size:6.3px;line-height:1.3}
.reward .note{border-top:1px dotted rgba(255,255,255,.7);margin-top:5px;padding-top:5px}

/* Consequences */
.poster-consequences .kicker{height:21px;font-size:16px;line-height:22px}
.poster-consequences .title-band{height:65px}
.poster-consequences .title{font-size:52px;line-height:65px}
.poster-consequences .motto{top:86px;height:26px;font-size:13.5px;line-height:26px}
.poster-consequences .brand{left:22px;top:34px}
.poster-consequences .brand-name{font-size:10px;width:64px}
.poster-consequences .brand-square{width:14px;height:14px}
.poster-consequences .footer{height:32px;font-size:11.5px;line-height:34px}
.poster-consequences .globe{width:16px;height:16px;margin-left:-8px;top:-8px}
.steps-bar{position:absolute;left:0;top:157px}
.step{position:absolute;top:157px;height:113px;text-align:center;color:#fff;padding-top:22px}
.step-num{font-weight:700;font-size:13.5px}
.step-name{font-weight:700;font-size:8.6px;line-height:1.1;margin-top:7px;text-transform:uppercase}
.step-icon{position:absolute;top:127px;width:44px;height:44px;margin-left:-22px;border-radius:50%;background:#fff;border:2px solid var(--lavender);display:flex;align-items:center;justify-content:center;color:var(--grape);z-index:2}
.grid{position:absolute;left:18px;top:271px;width:683px;height:187px;display:grid;grid-template-columns:102px 98px 96px 98px 97px 98px 94px;grid-template-rows:106px 81px}
.grid div{font-size:8.6px;line-height:1.25;padding:8px 6px 0}
.grid .head{background:var(--plum);color:#fff;font-weight:900;font-size:10px;line-height:1.05;padding:10px 9px}
.grid .light{background:var(--lavender)}
.grid .white{background:#fff}
.grid .top{border-bottom:1.5px dotted var(--magenta)}
.grid b{font-weight:900}
</style>
</head>
<body>

<!-- RULES -->
<section class="poster poster-rules">
  <div class="kicker">THE ALDWICK WAY</div>
  <div class="title-band"><h1 class="title">RULES</h1></div>
  <div class="brand"><span class="brand-square"></span><span class="brand-name">ALDWICK HOLLINS</span></div>
  <div class="motto">“HELPING US BE THE BEST WE CAN BE”</div>

  <div class="rule rule-ready">
    <div class="rule-column"></div>
    <div class="rule-pennant tone-mauve"><svg width="24" height="24" viewBox="0 0 24 24" fill="none" stroke="#fff" stroke-width="1.6"><circle cx="12" cy="12" r="9"/><path d="M12 7v5l3 2"/></svg></div>
    <div class="rule-label tone-mauve"><span style="color:#fff">BE<br>READY</span></div>
    <ul class="rule-list"><li>Punctual to<br>meet and greet</li><li>Ready to<br>learn new ideas</li><li>Be<br>Well-Presented</li><li>Have the right<br>equipment</li><li>Know<br>your seat</li></ul>
  </div>

  <div class="rule rule-respect">
    <div class="rule-column"></div>
    <div class="rule-pennant tone-magenta"><svg width="26" height="24" viewBox="0 0 26 24" fill="none" stroke="#fff" stroke-width="1.6"><path d="M13 21 3.5 11.5A5 5 0 0 1 13 5a5 5 0 0 1 9.5 6.5z"/></svg></div>
    <div class="rule-label tone-magenta"><span style="color:#fff">BE<br>RESPECTFUL</span></div>
    <ul class="rule-list"><li>Raise your hand<br>to talk</li><li>Manners give<br>a great impression</li><li>Hold doors<br>open for others</li><li>Respect every<br>persons right<br>to learn and work</li><li>Show the best<br>version of you</li><li>Be respectful<br>of everyone's<br>uniqueness.</li></ul>
  </div>

  <div class="rule rule-safe">
    <div class="rule-column"></div>
    <div class="rule-pennant tone-deep"><svg width="24" height="26" viewBox="0 0 24 26" fill="none" stroke="#fff" stroke-width="1.6"><path d="M12 2 3 5v7c0 6 4 10 9 12 5-2 9-6 9-12V5z"/><path d="m7.5 13 3 3 6-6"/></svg></div>
    <div class="rule-label tone-deep"><span style="color:#fff">BE<br>SAFE</span></div>
    <ul class="rule-list"><li>Walk quietly<br>around the school<br>building &amp; grounds</li><li>Throw litter<br>in the bin</li><li>Eat and drink<br>in the<br>designated areas</li><li>Leave your<br>desk tidy<br>for the next class</li><li>Look after our<br>building &amp; grounds</li></ul>
  </div>

  <div class="footer"><span class="globe"></span>www.aldwickhollins.org</div>
  <div class="footer-strip"></div>
</section>

<!-- REWARDS -->
<section class="poster poster-rewards">
  <div class="kicker">THE ALDWICK WAY</div>
  <div class="title-band"><h1 class="title">REWARDS</h1></div>
  <div class="brand"><span class="brand-square"></span><span class="brand-name">ALDWICK HOLLINS</span></div>
  <div class="motto">“CELEBRATING WHEN WE ARE AT OUR BEST”</div>

  <div class="reward reward-house">
    <span class="reward-badge"><svg width="22" height="22" viewBox="0 0 24 24" fill="none" stroke="currentColor" stroke-width="1.6"><path d="m12 3 2.6 5.6 6 .7-4.5 4.1 1.2 6L12 16.4 6.7 19.4l1.2-6L3.4 9.3l6-.7z"/></svg></span>
    <h3>HOUSE POINTS</h3>
    <p style="margin-top:8px">Class Teachers can award house points for great learning, participating in clubs, acts of kindness, going above the expected standard</p>
    <p class="note">House Points can be spent in the school shop</p>
  </div>

  <div class="reward reward-council">
    <span class="reward-badge"><svg width="22" height="24" viewBox="0 0 24 26" fill="none" stroke="currentColor" stroke-width="1.6"><circle cx="12" cy="9" r="6.5"/><path d="m8 14.5-2 9 6-3 6 3-2-9"/></svg></span>
    <h3>SCHOOL COUNCILLOR CERTIFICATES</h3>
    <div class="points">10 HOUSE POINTS</div>
    <p>Anyone can recommend a certificate for their peer in recognition of a positive behaviour choice.</p>
    <p class="note">A certificate is awarded in assembly and sent to your family</p>
  </div>

  <div class="reward reward-subject">
    <span class="reward-badge"><svg width="24" height="20" viewBox="0 0 26 22" fill="none" stroke="currentColor" stroke-width="1.6"><rect x="2" y="2" width="22" height="16" rx="1"/><path d="M6 7h10M6 11h7"/><circle cx="19" cy="13" r="2.5"/></svg></span>
    <h3>SUBJECT LEADER CERTIFICATES</h3>
    <div class="points">10 HOUSE POINTS</div>
    <p>Subject Leaders can award certificates for great subject knowledge and learning</p>
    <p class="note">A certificate is awarded in assembly and sent to your family</p>
  </div>

  <div class="reward reward-head">
    <span class="reward-badge"><svg width="22" height="20" viewBox="0 0 24 22" fill="none" stroke="currentColor" stroke-width="1.6"><path d="M3 17 2 6l6 5 4-7 4 7 6-5-1 11z"/><path d="M3 20h18"/></svg></span>
    <h3>HEAD OF YEAR CERTIFICATES</h3>
    <div class="points">20 HOUSE POINTS</div>
    <p>Heads of Year award certificates for outstanding learners who have excelled in more than one area.</p>
    <p class="note">A certificate is awarded in assembly and sent to your family. You will have a hot chocolate with the head teacher</p>
  </div>

  <div class="footer"><span class="globe"></span>www.aldwickhollins.org</div>
  <div class="footer-strip"></div>
</section>

<!-- CONSEQUENCES -->
<section class="poster poster-consequences">
  <div class="kicker">THE ALDWICK WAY</div>
  <div class="title-band"><h1 class="title">CONSEQUENCES</h1></div>
  <div class="brand"><span class="brand-square"></span><span class="brand-name">ALDWICK HOLLINS</span></div>
  <div class="motto">“LEARNING FROM OUR MISTAKES TO BE OUR BEST”</div>

  <svg class="steps-bar" width="720" height="113" viewBox="0 0 720 113" aria-hidden="true">
    <polygon points="101,0 218,0 230,56.5 218,113 101,113 113,56.5" fill="#8a6f86"/>
    <polygon points="218,0 314,0 326,56.5 314,113 218,113 230,56.5" fill="#a34d96"/>
    <polygon points="314,0 412,0 424,56.5 412,113 314,113 326,56.5" fill="#b52fa0"/>
    <polygon points="412,0 509,0 521,56.5 509,113 412,113 424,56.5" fill="#8c2b7f"/>
    <polygon points="509,0 607,0 619,56.5 607,113 509,113 521,56.5" fill="#6e2a5f"/>
    <polygon points="607,0 696,0 708,56.5 696,113 607,113 619,56.5" fill="#3e2230"/>
  </svg>

  <span class="step-icon" style="left:169px"><svg width="22" height="22" viewBox="0 0 24 24" fill="none" stroke="currentColor" stroke-width="1.7"><circle cx="14" cy="10" r="6"/><path d="m9.5 14.5-6 6"/></svg></span>
  <span class="step-icon" style="left:270px"><svg width="20" height="22" viewBox="0 0 22 24" fill="none" stroke="currentColor" stroke-width="1.7"><path d="M5 22V3M5 4h12l-3 4 3 4H5"/></svg></span>
  <span class="step-icon" style="left:367px"><svg width="22" height="20" viewBox="0 0 24 22" fill="none" stroke="currentColor" stroke-width="1.7"><path d="M12 2 1.5 20h21z"/><path d="M12 8v6M12 16.5v1.5"/></svg></span>
  <span class="step-icon" style="left:465px"><svg width="22" height="22" viewBox="0 0 24 24" fill="none" stroke="currentColor" stroke-width="1.7"><rect x="3" y="3" width="18" height="18" rx="3"/><circle cx="8" cy="8" r="1" fill="currentColor"/><circle cx="16" cy="16" r="1" fill="currentColor"/><circle cx="12" cy="12" r="1" fill="currentColor"/></svg></span>
  <span class="step-icon" style="left:560px"><svg width="22" height="22" viewBox="0 0 24 24" fill="none" stroke="currentColor" stroke-width="1.7"><path d="M20 12a8 8 0 1 1-3-6.2"/><path d="M18 2v5h-5"/></svg></span>
  <span class="step-icon" style="left:654px"><svg width="22" height="22" viewBox="0 0 24 24" fill="none" stroke="currentColor" stroke-width="1.7"><circle cx="12" cy="12" r="3.5"/><path d="M12 2v3M12 19v3M2 12h3M19 12h3M4.9 4.9 7 7M17 17l2.1 2.1M4.9 19.1 7 17M17 7l2.1-2.1"/></svg></span>

  <div class="step" style="left:116px;width:106px"><div class="step-num">STEP 1</div><div class="step-name">Recognizing your behaviour is stopping you or others learn</div></div>
  <div class="step" style="left:228px;width:90px"><div class="step-num">STEP 2</div><div class="step-name">Reminder<br>of<br>expectations</div></div>
  <div class="step" style="left:326px;width:90px"><div class="step-num">STEP 3</div><div class="step-name">Caution</div></div>
  <div class="step" style="left:424px;width:90px"><div class="step-num">STEP 4</div><div class="step-name">Last<br>chance</div></div>
  <div class="step" style="left:521px;width:90px"><div class="step-num">STEP 5</div><div class="step-name">Consequence</div></div>
  <div class="step" style="left:619px;width:82px"><div class="step-num">STEP 6</div><div class="step-name">Repair</div></div>

  <div class="grid">
    <div class="head top">HOW CAN<br>I HELP<br>MYSELF?</div>
    <div class="white top">Refocus on my learning. Seek help if I don't understand the learning task <b>and show me at my best.</b></div>
    <div class="light top">Listen to the reminder and refocus on my learning. Seek help if I don't understand the learning task <b>and still show the best me.</b></div>
    <div class="white top">Listen to the choice and consequence and refocus on my learning <b>and still show the best me.</b></div>
    <div class="light top">Listen to the choice and consequence and refocus on my learning – <b>and still show the best me.</b></div>
    <div class="white top">Accept the consequence <b>and still show the best me.</b></div>
    <div class="light top">Work with the teachers and peers to reflect on my choices and share what was happening for me.</div>
    <div class="head">HOW CAN<br>MY TEACHER<br>HELP ME?</div>
    <div class="white">Help me understand the learning task and what is expected of me. Ask me if there's a problem'</div>
    <div class="light">Remind me of the rules, delivered privately</div>
    <div class="white">Remind me of the rules, delivered privately</div>
    <div class="light">Give a 'choice &amp; consequence' and some take up time</div>
    <div class="white">Give a consequence and an opportunity to repair</div>
    <div class="light">Discuss how to help me make better choices next time.</div>
  </div>

  <div class="footer"><span class="globe"></span>www.aldwickhollins.org</div>
  <div class="footer-strip"></div>
</section>

</body>
</html>
```